R & T Summit Construction Business Card ideas

We want a business card to represents our company in a way that looks professional but is also a business card that is unique!

Industry/Entity Type

Construction Company

Contact Information for Business Card

open to all design ideas, just want to be able to see different options to choose from in either color or grayscale.

Requirements
Must have
• Our names and phone numbers
• Nolan Pritchett 512-804-2271
• Curtis Hale 512-693-1804
• Business logo

```html
<!DOCTYPE html>
<html lang="en">
<head>
<meta charset="utf-8">
<title>R & T Summit Construction – Business Card</title>
<link rel="stylesheet" href="https://fonts.googleapis.com/css2?family=Montserrat:wght@700&family=Questrial&display=swap">
<style>
  :root {
    --backdrop: #2b2b2b;
    --ink: #111111;
    --ink-soft: #555555;
    --paper-top: #ffffff;
    --paper-bottom: #d9d9d9;
    --card-dark: #050505;
    --logo-light: #e6e6e6;
    --rule: #b5b5b5;
  }
  * { box-sizing: border-box; margin: 0; padding: 0; }
  html, body {
    width: 1200px; height: 929px; overflow: hidden;
    background: var(--backdrop);
    font-family: "Questrial", sans-serif;
  }
  .canvas { position: relative; width: 1200px; height: 929px; }
  .card {
    position: absolute; width: 560px; height: 320px;
    box-shadow: 0 12px 30px rgba(0,0,0,0.45);
  }
  .card--back {
    left: 80px; top: 90px;
    background: var(--card-dark);
    display: flex; align-items: center; justify-content: center;
  }
  .card--front {
    left: 560px; top: 510px;
    background: linear-gradient(135deg, var(--paper-top) 0%, #eeeeee 55%, var(--paper-bottom) 100%);
    display: grid; grid-template-columns: 330px 1px 1fr;
  }
  .brand {
    display: flex; align-items: center; gap: 12px;
    font-family: "Questrial", sans-serif; font-size: 26px; line-height: 1.15;
  }
  .brand__mark { width: 18px; height: 18px; flex: none; }
  .card--back .brand { color: var(--logo-light); }
  .card--back .brand__mark { background: var(--logo-light); }
  .card--front .brand { color: var(--ink); justify-content: center; padding: 0 20px; font-size: 23px; }
  .card--front .brand__mark { background: var(--ink); }
  .divider { background: var(--rule); margin: 24px 0; }
  .details { padding: 52px 0 0 30px; color: var(--ink-soft); font-size: 14px; }
  .details__name {
    font-family: "Montserrat", sans-serif; font-weight: 700;
    font-size: 16px; color: var(--ink); letter-spacing: 0.5px;
  }
  .details__title { margin-top: 2px; }
  .contact { list-style: none; margin-top: 26px; }
  .contact li { display: flex; align-items: center; gap: 8px; line-height: 20px; }
  .contact svg { width: 12px; height: 12px; fill: var(--ink); flex: none; }
  .details__address { margin-top: 24px; line-height: 18px; }
</style>
</head>
<body>
<div class="canvas">
  <section class="card card--back">
    <div class="brand"><span class="brand__mark"></span><span>R &amp; T Summit Construction</span></div>
  </section>

  <section class="card card--front">
    <div class="brand"><span class="brand__mark"></span><span>R &amp; T Summit Construction</span></div>
    <div class="divider"></div>
    <div class="details">
      <p class="details__name">NOLAN PRITCHETT</p>
      <p class="details__title">Managing Director</p>
      <ul class="contact">
        <li><svg viewBox="0 0 24 24"><path d="M6.6 10.8a15.1 15.1 0 0 0 6.6 6.6l2.2-2.2c.3-.3.7-.4 1-.2 1.1.4 2.3.6 3.6.6.6 0 1 .4 1 1V20c0 .6-.4 1-1 1C10.6 21 3 13.4 3 4c0-.6.4-1 1-1h3.5c.6 0 1 .4 1 1 0 1.3.2 2.5.6 3.6.1.3 0 .7-.2 1z"/></svg>512-804-2271</li>
        <li><svg viewBox="0 0 24 24"><path d="M2 5h20v14H2z M4 7v.5l8 5 8-5V7z" fill-rule="evenodd"/></svg>info@rtsummit.com</li>
        <li><svg viewBox="0 0 24 24"><path d="M12 2a10 10 0 1 0 0 20 10 10 0 0 0 0-20zm0 2c.9 1.2 1.6 2.8 1.9 4.5h-3.8C10.4 6.8 11.1 5.2 12 4zm-7.4 9.5a8 8 0 0 1 0-3h3.6a17 17 0 0 0 0 3zm1 2h3c.3 1.6.8 3 1.5 4.1a8 8 0 0 1-4.5-4.1zm3-7h-3a8 8 0 0 1 4.5-4.1C9.4 5.5 8.9 6.9 8.6 8.5zM12 20c-.9-1.2-1.6-2.8-1.9-4.5h3.8c-.3 1.7-1 3.3-1.9 4.5zm2.2-6.5H9.8a15 15 0 0 1 0-3h4.4a15 15 0 0 1 0 3zm.3 6.1c.7-1.1 1.2-2.5 1.5-4.1h3a8 8 0 0 1-4.5 4.1zm1.3-6.1a17 17 0 0 0 0-3h3.6a8 8 0 0 1 0 3z"/></svg>www.rtsummit.com</li>
      </ul>
      <p class="details__address">Here your company<br>or home address</p>
    </div>
  </section>
</div>
</body>
</html>
```